Agriculture Security Company needs a business card design

We need a business card design for a new company based in Seattle calls Corvantel Guard LLC. We provide high-end physical security solutions that is geared and focused towards to the marijuana grow operations, wholesalers and distributors. We DO NOT get involved in the retail operations (store fronts). We would like to see designs that incorporate professionalism, reliability, trustworthy and forward thinking as traits of our organization.

Industry/Entity Type

Security

```html
<!DOCTYPE html>
<html lang="en">
<head>
<meta charset="utf-8">
<title>Corvantel Guard LLC — Business Card</title>
<link href="https://fonts.googleapis.com/css2?family=Montserrat:wght@400;500;600&display=swap" rel="stylesheet">
<style>
  :root {
    --stage: #2b2b2d;
    --forest: #06573a;
    --forest-deep: #044a31;
    --forest-soft: #0b6442;
    --leaf: #5f9a2f;
    --paper: #ffffff;
    --paper-shade: #eeeeee;
    --ink: #6b6e73;
  }
  * { margin: 0; padding: 0; box-sizing: border-box; }
  html, body { width: 1200px; height: 900px; overflow: hidden; }
  body {
    background: var(--stage);
    font-family: "Montserrat", Arial, sans-serif;
    display: flex;
    flex-direction: column;
    align-items: center;
    justify-content: center;
    gap: 44px;
  }
  .card {
    position: relative;
    width: 700px;
    height: 400px;
    border-radius: 30px;
    overflow: hidden;
    box-shadow: 0 12px 30px rgba(0,0,0,.45);
  }
  .card-back { background: var(--forest); }
  .card-back .swoosh { position: absolute; inset: 0; width: 100%; height: 100%; }
  .card-back .brand {
    position: absolute;
    left: 0; right: 0; top: 150px;
    text-align: center;
  }
  .brand-name {
    font-weight: 600;
    color: var(--leaf);
    letter-spacing: .02em;
  }
  .card-back .brand-name { font-size: 50px; }
  .brand-tagline {
    font-weight: 500;
    color: var(--leaf);
    text-transform: uppercase;
    letter-spacing: .14em;
  }
  .card-back .brand-tagline { font-size: 15px; margin-top: 8px; }

  .card-front {
    background: linear-gradient(160deg, var(--paper) 40%, var(--paper-shade) 100%);
  }
  .card-front .band {
    position: absolute;
    left: 0; right: 0; bottom: 0;
    height: 40px;
    background: var(--forest);
  }
  .card-front .brand { position: absolute; left: 46px; top: 46px; }
  .card-front .brand-name { font-size: 30px; color: var(--forest); }
  .card-front .brand-tagline { font-size: 10px; margin-top: 5px; }
  .contact {
    position: absolute;
    left: 400px; top: 128px;
  }
  .contact-name { font-size: 20px; font-weight: 500; color: var(--leaf); }
  .contact-role { font-size: 13px; color: var(--ink); margin: 4px 0 16px 4px; }
  .contact-list { list-style: none; font-size: 14px; color: var(--ink); line-height: 1.6; }
  .contact-list .key { display: inline-block; width: 20px; color: var(--leaf); font-weight: 600; }
  .address {
    position: absolute;
    left: 46px; bottom: 78px;
    font-size: 16px; color: var(--ink); line-height: 1.45;
    font-style: normal;
  }
  .address-label { color: var(--leaf); font-weight: 500; font-size: 15px; }
</style>
</head>
<body>

<section class="card card-back" aria-label="Card back">
  <svg class="swoosh" viewBox="0 0 700 400" preserveAspectRatio="none" aria-hidden="true">
    <path d="M0 250 C180 150 420 70 700 40 L700 0 L0 0 Z" fill="var(--forest-soft)" opacity=".55"/>
    <path d="M0 400 L0 330 C200 260 430 200 700 180 L700 400 Z" fill="var(--forest-deep)" opacity=".6"/>
  </svg>
  <div class="brand">
    <div class="brand-name">Corvantel Guard</div>
    <div class="brand-tagline">Securing the Harvest</div>
  </div>
</section>

<section class="card card-front" aria-label="Card front">
  <div class="brand">
    <div class="brand-name">Corvantel Guard</div>
    <div class="brand-tagline">Securing the Harvest</div>
  </div>

  <div class="contact">
    <div class="contact-name">Daniel Okerlund</div>
    <div class="contact-role">managing director</div>
    <ul class="contact-list">
      <li><span class="key">P</span>206 555 01 42</li>
      <li><span class="key">M</span>206 555 01 87</li>
      <li><span class="key">E</span>dokerlund@corvantelguard.com</li>
      <li><span class="key">W</span>www.corvantelguard.com</li>
    </ul>
  </div>

  <address class="address">
    <div class="address-label">Address:</div>
    418 Harbor Lane<br>
    Seattle, Washington 98101
  </address>

  <div class="band"></div>
</section>

</body>
</html>
```